Business Card Design Project

Use our current logo. Clean design.

Industry/Entity Type

Business

Requirements
Must have
• Marisela DUBRANCQ
M. Law
Managing Partner

Alpenvorsa AG
Kornhalmweg 214
CH-3097 Liebefeld

M. +41 79 412 56 27
T. +41 31 928 44 10
F. +41 31 928 44 19

m.dubrancq@alpenvorsa-example.com
www.alpenvorsa-example.com

```html
<!DOCTYPE html>
<html lang="en">
<head>
<meta charset="utf-8">
<title>Alpenvorsa AG – Business Card</title>
<link rel="stylesheet" href="https://fonts.googleapis.com/css2?family=Marcellus&family=Crimson+Text&family=Arimo&display=swap">
<style>
  :root {
    --ink: #231f20;
    --accent: #cc0000;
    --paper: #ffffff;
    --rule: #000000;
  }
  * { margin: 0; padding: 0; box-sizing: border-box; }
  html, body { width: 1050px; height: 1200px; overflow: hidden; background: var(--paper); }
  .sheet { position: relative; width: 1050px; height: 1200px; background: var(--paper); }

  .brand-name {
    position: absolute;
    font-family: "Marcellus", serif;
    color: var(--ink);
    letter-spacing: 0.02em;
    white-space: nowrap;
    line-height: 1;
  }
  .card-front .brand-name { left: 0; width: 1050px; top: 250px; text-align: center; font-size: 92px; }
  .website {
    position: absolute; left: 0; width: 1060px; top: 444px; text-align: center;
    font-family: "Arimo", sans-serif; font-size: 22px; color: var(--accent);
  }

  .divider { position: absolute; left: 0; top: 594px; width: 1050px; height: 10px; background: var(--rule); }

  .card-back .brand-name { left: 80px; width: 506px; top: 815px; text-align: center; font-size: 64px; }

  .contact-row { position: absolute; left: 633px; }
  .contact-row svg { position: absolute; left: 0; top: 0; }
  .contact-text {
    position: absolute; left: 63px; top: 0; white-space: nowrap;
    font-family: "Crimson Text", serif; font-size: 13.5px; line-height: 17.5px; color: var(--accent);
  }
  .row-person { top: 676px; }
  .row-person .role { margin-top: 3px; }
  .row-address { top: 776px; }
  .row-phone { top: 871px; }
  .row-phone .contact-text { top: 9px; }
  .row-mail { top: 974px; }
  .row-mail .contact-text { top: 42px; }
</style>
</head>
<body>
<main class="sheet">
  <section class="card-front">
    <div class="brand-name">ALPENVORSA</div>
    <div class="website">www.alpenvorsa-example.com</div>
  </section>

  <div class="divider"></div>

  <section class="card-back">
    <div class="brand-name">ALPENVORSA</div>

    <div class="contact-row row-person">
      <svg width="44" height="52" viewBox="0 0 44 52" aria-hidden="true">
        <circle cx="21" cy="10" r="10" fill="#000"/>
        <path d="M14 18 C14 30 2 36 0 50 L43 50 C41 36 29 30 29 18 Z" fill="#000"/>
      </svg>
      <div class="contact-text">
        <div>Marisela DUBRANCQ</div>
        <div>M. Law</div>
        <div class="role">Managing Partner</div>
      </div>
    </div>

    <div class="contact-row row-address">
      <svg width="46" height="52" viewBox="0 0 46 52" aria-hidden="true">
        <path d="M23 0 L46 18 L46 22 L42 22 L42 50 L29 50 L29 36 L17 36 L17 50 L4 50 L4 22 L0 22 L0 18 Z" fill="#000"/>
      </svg>
      <div class="contact-text">
        <div>Alpenvorsa AG</div>
        <div>Kornhalmweg 214</div>
        <div>CH-3097 Liebefeld</div>
      </div>
    </div>

    <div class="contact-row row-phone">
      <svg width="44" height="60" viewBox="0 0 44 60" aria-hidden="true">
        <rect x="3" y="0" width="38" height="58" rx="6" fill="#000"/>
        <rect x="10" y="9" width="24" height="36" rx="3" fill="#fff"/>
        <rect x="17" y="3" width="10" height="2" rx="1" fill="#fff"/>
        <circle cx="22" cy="51" r="2.5" fill="#fff"/>
      </svg>
      <div class="contact-text">
        <div>M.&nbsp; +41 79 412 56 27</div>
        <div>T.&nbsp;&nbsp; +41 31 928 44 10</div>
        <div>F.&nbsp;&nbsp; +41 31 928 44 19</div>
      </div>
    </div>

    <div class="contact-row row-mail">
      <svg width="50" height="58" viewBox="0 0 50 58" aria-hidden="true">
        <rect x="5" y="1" width="42" height="54" fill="none" stroke="#000" stroke-width="1.5"/>
        <path d="M5 1 L26 38 L47 1 M5 55 L26 38 L47 55" fill="none" stroke="#000" stroke-width="1.2"/>
      </svg>
      <div class="contact-text">m.dubrancq@alpenvorsa-example.com</div>
    </div>
  </section>
</main>
</body>
</html>
```